Marketing Postcards

I recently changed real estate companies and want to redo some advertising postcards I've used in the past. I want to replicate the existing cards with updated company info. Please see attached for proofs of old cards as well as the new company logo.

Industry/Entity Type

Real Estate

```html
<!DOCTYPE html>
<html lang="en">
<head>
<meta charset="utf-8">
<title>Marla Quinn – Postcard Series</title>
<link href="https://fonts.googleapis.com/css2?family=Oswald:wght@300;500;600&family=Open+Sans:wght@400;700&display=swap" rel="stylesheet">
<style>
  :root{
    --board:#4b2616;
    --plum:#4a2748;
    --panel:#43293f;
    --panel-text:#ece4ea;
    --ink:#1d1a1c;
    --grey:#8b8589;
    --white:#ffffff;
  }
  *{box-sizing:border-box;margin:0;padding:0}
  html,body{width:900px;height:1200px;overflow:hidden}
  body{background:var(--board);position:relative;font-family:"Open Sans",Arial,sans-serif}

  .label{position:absolute;color:var(--white);font-family:"Open Sans",Arial,sans-serif;font-weight:700;font-size:31px;letter-spacing:.5px;transform:translateX(-50%);white-space:nowrap}
  .label.back-label{font-size:56px;transform:none}

  .card{position:absolute;background:var(--panel);box-shadow:0 3px 10px rgba(0,0,0,.45);overflow:hidden}
  .side{position:absolute;left:0;top:0;bottom:0;width:62%;border-right:3px solid var(--white)}
  .photo{position:absolute;inset:0}
  .shapes{position:absolute;inset:0;width:100%;height:100%}

  .header{position:absolute;left:0;top:0;right:0;height:50%}
  .portrait{position:absolute;left:7px;top:9px;width:46px;height:58px;border:1px solid #b9b2b7;background:linear-gradient(160deg,#9a8a86,#3d5a92 70%,#2c4478)}
  .contact{position:absolute;left:59px;top:9px;width:88px;line-height:1}
  .call{font-family:"Oswald",sans-serif;font-weight:300;font-size:9px;color:var(--grey)}
  .name{font-family:"Oswald",sans-serif;font-weight:600;font-size:10.5px;color:var(--plum);margin-top:3px;letter-spacing:.2px}
  .phone{font-family:"Oswald",sans-serif;font-weight:600;font-size:14px;color:var(--ink);margin-top:1px;letter-spacing:-.3px;white-space:nowrap}
  .web{font-size:3.9px;color:var(--ink);margin-top:3px;line-height:1.35;white-space:nowrap}
  .tagline{font-family:"Oswald",sans-serif;font-weight:500;font-size:7.5px;color:var(--ink);margin-top:3px;line-height:1.2}

  .brand{position:absolute;right:5px;top:8px;width:50px}
  .brand-mark{display:block;width:22px;height:22px;border-radius:50%;border:2px solid var(--plum);margin:0 auto}
  .brand-name{font-size:4.6px;font-weight:700;color:var(--plum);margin-top:2px;line-height:1.15;text-align:center}
  .address{font-family:"Oswald",sans-serif;font-weight:500;font-size:4.8px;color:var(--ink);margin-top:5px;line-height:1.3;text-align:left;white-space:nowrap}

  .panel{position:absolute;top:0;right:0;bottom:0;width:38%;padding:14px 9px 6px 9px;color:var(--panel-text);font-size:5.6px;line-height:1.34;text-align:justify}
  .panel p{margin-bottom:5px}
  .panel h3{font-family:"Oswald",sans-serif;font-weight:500;font-size:6px;color:var(--white);text-transform:uppercase;margin:3px 0 3px;text-align:left;line-height:1.2}

  .card.back{background:var(--white)}
  .back .divider{position:absolute;left:206px;top:0;bottom:0;width:2px;background:var(--plum)}
  .back .stamp{position:absolute;left:290px;top:12px;width:46px;height:45px;border:1px solid #555}
  .back .header{height:110px;width:206px}
  .back .portrait{left:14px;top:14px;width:40px;height:52px}
  .back .contact{left:60px;top:14px}
  .back .brand{right:4px;top:10px;width:48px}
  .back .tagline{white-space:nowrap}
  .pledge{position:absolute;left:0;top:110px;width:206px;height:92px;background:var(--plum);border-radius:0 14px 14px 0;color:var(--panel-text);padding:8px 11px 0 14px;font-size:6.4px;line-height:1.3;text-align:justify}
  .pledge h3{font-family:"Open Sans",sans-serif;font-weight:700;font-size:6.8px;color:var(--white);margin-bottom:4px;white-space:nowrap}
</style>
</head>
<body>

<div class="label" style="left:260px;top:34px">FRONT 1</div>
<div class="card" style="left:80px;top:74px;width:344px;height:232px">
  <div class="side">
    <div class="photo" role="img" aria-label="Photo of a living room with fireplace and grey walls" style="background:linear-gradient(180deg,#bfc4c9 40%,#8b8d92 70%,#4b3a30)"></div>
    <svg class="shapes" viewBox="0 0 100 100" preserveAspectRatio="none"><polygon points="0,0 100,0 100,42 58,54 0,46" fill="#fff"/><polygon points="0,46 58,54 100,42 100,47 58,59 0,51" fill="#4a2748"/></svg>
    <div class="header">
      <div class="portrait" role="img" aria-label="Agent portrait"></div>
      <div class="contact"><div class="call">Call Today!</div><div class="name">MARLA QUINN</div><div class="phone">555-014-2290</div><div class="web">hello@marlaquinnhomes.com<br>www.harborcountyhomes.example</div><div class="tagline">With you every step<br>of the way!</div></div>
      <div class="brand"><span class="brand-mark"></span><div class="brand-name">Harbor Point Homes</div><div class="address">1820 Harbor Lane<br>Bayport, NC 28500</div></div>
    </div>
  </div>
  <div class="panel" style="padding-top:22px">
    <p>Realize the full benefits of entering today's high performing real estate market.</p>
    <p>Start with an accurate assessment and a highly customized marketing plan.</p>
    <p>As one of the top real estate agents in Harbor County, Marla Quinn is uniquely qualified to identify opportunity and manage exceptional results. Each assessment and marketing strategy is as unique as the individual's property and future plans.</p>
    <p>Client relationships are confidential and based on supporting and often exceeding desired results.</p>
    <p>To contact me, please use the information on this card.</p>
  </div>
</div>

<div class="label" style="left:662px;top:34px">FRONT 2</div>
<div class="card" style="left:492px;top:74px;width:340px;height:228px">
  <div class="side">
    <div class="photo" role="img" aria-label="Photo of a kitchen with dark wood floors and brick wall" style="background:linear-gradient(180deg,#e8e4de 40%,#7a6a5c 70%,#3a2a22)"></div>
    <svg class="shapes" viewBox="0 0 100 100" preserveAspectRatio="none"><polygon points="0,0 100,0 100,42 58,54 0,46" fill="#fff"/><polygon points="0,46 58,54 100,42 100,47 58,59 0,51" fill="#4a2748"/></svg>
    <div class="header">
      <div class="portrait" role="img" aria-label="Agent portrait"></div>
      <div class="contact"><div class="call">Call Today!</div><div class="name">MARLA QUINN</div><div class="phone">555-014-2290</div><div class="web">hello@marlaquinnhomes.com<br>www.harborcountyhomes.example</div><div class="tagline">With you every step<br>of the way!</div></div>
      <div class="brand"><span class="brand-mark"></span><div class="brand-name">Harbor Point Homes</div><div class="address">1820 Harbor Lane<br>Bayport, NC 28500</div></div>
    </div>
  </div>
  <div class="panel" style="padding-top:9px">
    <p>Time to move? Engage in a highly customized search and transitional plan tailor-fitted to your objective.</p>
    <p>Whether you are interested in downsizing, acquiring more space, staying in your current community or moving elsewhere – Marla Quinn brings experience and commitment to cultivate your desired outcome.</p>
    <p>As one of the top real estate agents in Harbor County, Marla is uniquely qualified to orchestrate your new home search and maximize your property sale. Marla brings an exceptional network of professionals locally and throughout the country to support your best interests within your timeframe.</p>
    <p>Client relationships are confidential and based on exceeding desired results.</p>
    <p>To contact me, please use the information on this card.</p>
  </div>
</div>

<div class="label" style="left:250px;top:322px">FRONT 3</div>
<div class="card" style="left:84px;top:364px;width:338px;height:228px">
  <div class="side">
    <div class="photo" role="img" aria-label="Photo of kitchen cabinets with tile backsplash" style="background:linear-gradient(180deg,#c98a45 45%,#7a6c68 70%,#2a2523)"></div>
    <svg class="shapes" viewBox="0 0 100 100" preserveAspectRatio="none"><polygon points="0,0 100,0 100,42 58,54 0,46" fill="#fff"/><polygon points="0,46 58,54 100,42 100,47 58,59 0,51" fill="#4a2748"/></svg>
    <div class="header">
      <div class="portrait" role="img" aria-label="Agent portrait"></div>
      <div class="contact"><div class="call">Call Today!</div><div class="name">MARLA QUINN</div><div class="phone">555-014-2290</div><div class="web">hello@marlaquinnhomes.com<br>www.harborcountyhomes.example</div><div class="tagline">With you every step<br>of the way!</div></div>
      <div class="brand"><span class="brand-mark"></span><div class="brand-name">Harbor Point Homes</div><div class="address">1820 Harbor Lane<br>Bayport, NC 28500</div></div>
    </div>
  </div>
  <div class="panel" style="padding-top:9px">
    <h3>Professional staging and compelling marketing materials</h3>
    <p>All staging, photography, brochures, and custom websites are done by a team of professionals to maximize the positive aspects of your home.</p>
    <h3>Targeted marketing to your best audience</h3>
    <p>Custom for each property utilizing diverse and targeted mediums including transitional print ads, electronic marketing, and advanced social media advertising.</p>
    <h3>Preferred vendor program</h3>
    <p>To fill voids in services needed pre- and post-sales. Our team of professionals will make selling your home seamless.</p>
    <p>Each assessment is confidential, as custom as the individual property and backed by exceptional results. To learn more, please contact me using the information on this card.</p>
  </div>
</div>

<div class="label" style="left:662px;top:324px">FRONT 4</div>
<div class="card" style="left:488px;top:366px;width:346px;height:232px">
  <div class="side">
    <div class="photo" role="img" aria-label="Photo of a bright kitchen with red wood floor" style="background:linear-gradient(180deg,#eeeae2 45%,#b59a72 65%,#7a2f22)"></div>
    <svg class="shapes" viewBox="0 0 100 100" preserveAspectRatio="none"><polygon points="0,0 100,0 100,42 58,54 0,46" fill="#fff"/><polygon points="0,46 58,54 100,42 100,47 58,59 0,51" fill="#4a2748"/></svg>
    <div class="header">
      <div class="portrait" role="img" aria-label="Agent portrait"></div>
      <div class="contact"><div class="call">Call Today!</div><div class="name">MARLA QUINN</div><div class="phone">555-014-2290</div><div class="web">hello@marlaquinnhomes.com<br>www.harborcountyhomes.example</div><div class="tagline">With you every step<br>of the way!</div></div>
      <div class="brand"><span class="brand-mark"></span><div class="brand-name">Harbor Point Homes</div><div class="address">1820 Harbor Lane<br>Bayport, NC 28500</div></div>
    </div>
  </div>
  <div class="panel" style="padding-top:22px">
    <h3>Honest, comprehensive assessment</h3>
    <p>Known for her candid and thorough evaluations, Marla Quinn assures a solid foundation for future strategies.</p>
    <h3>Complete confidentiality</h3>
    <p>Your consent comes before any involvement of colleagues and/or industry professionals.</p>
    <h3>Regular communication</h3>
    <p>Initially pre-determined by your goals, then weekly when your home is market ready.</p>
    <p>As one of the top agents in Harbor County, Marla Quinn is uniquely qualified to help you. Each assessment is confidential, as custom as the individual property and backed by exceptional results. To learn more, please contact me using the</p>
  </div>
</div>

<div class="label" style="left:250px;top:628px">FRONT 5</div>
<div class="card" style="left:74px;top:670px;width:340px;height:228px">
  <div class="side">
    <div class="photo" role="img" aria-label="Photo of a kitchen with cream cabinets and open shelving" style="background:linear-gradient(180deg,#ece8e2 45%,#d6c08a 72%,#b89c62)"></div>
    <svg class="shapes" viewBox="0 0 100 100" preserveAspectRatio="none"><polygon points="0,0 100,0 100,42 58,54 0,46" fill="#fff"/><polygon points="0,46 58,54 100,42 100,47 58,59 0,51" fill="#4a2748"/></svg>
    <div class="header">
      <div class="portrait" role="img" aria-label="Agent portrait"></div>
      <div class="contact"><div class="call">Call Today!</div><div class="name">MARLA QUINN</div><div class="phone">555-014-2290</div><div class="web">hello@marlaquinnhomes.com<br>www.harborcountyhomes.example</div><div class="tagline">With you every step<br>of the way!</div></div>
      <div class="brand"><span class="brand-mark"></span><div class="brand-name">Harbor Point Homes</div><div class="address">1820 Harbor Lane<br>Bayport, NC 28500</div></div>
    </div>
  </div>
  <div class="panel" style="padding-top:24px">
    <p>Regardless of whether you plan to sell your home this year, or perhaps down the road, it is never too soon to have a real estate market analysis. Utilize our professional expertise to maximize the return of any future improvements you might be considering.</p>
    <p>As one of the top agents in Harbor County, Marla Quinn is uniquely qualified to provide the information you need to ensure your home continues to support your life plans.</p>
    <p>Each assessment is confidential, as custom as the individual property and backed by exceptional results. To learn more, please contact me using the information on this card.</p>
  </div>
</div>

<div class="label" style="left:670px;top:628px">FRONT 6</div>
<div class="card" style="left:492px;top:674px;width:340px;height:226px">
  <div class="side">
    <div class="photo" role="img" aria-label="Photo of a brick front porch with rocking chairs and green lawn" style="background:linear-gradient(100deg,#6f9a4a 0%,#9cbf6a 35%,#a4503a 60%,#f2f0ec 85%)"></div>
    <svg class="shapes" viewBox="0 0 100 100" preserveAspectRatio="none"><polygon points="0,0 100,0 100,42 58,54 0,46" fill="#fff"/><polygon points="0,46 58,54 100,42 100,47 58,59 0,51" fill="#4a2748"/></svg>
    <div class="header">
      <div class="portrait" role="img" aria-label="Agent portrait"></div>
      <div class="contact"><div class="call">Call Today!</div><div class="name">MARLA QUINN</div><div class="phone">555-014-2290</div><div class="web">hello@marlaquinnhomes.com<br>www.harborcountyhomes.example</div><div class="tagline">With you every step<br>of the way!</div></div>
      <div class="brand"><span class="brand-mark"></span><div class="brand-name">Harbor Point Homes</div><div class="address">1820 Harbor Lane<br>Bayport, NC 28500</div></div>
    </div>
  </div>
  <div class="panel" style="padding-top:28px">
    <h3>Internet exposure to the max</h3>
    <p>Known for her candid and thorough evaluations, Marla Quinn assures a solid foundation for future strategies.</p>
    <p>A recent university study showed that agents who contacted consumers who were inquiring about homes online within the first 5 minutes of registration have an extremely higher likelihood of converting that inquiry into a closed sale. Studies also show that 80% of buyers work with the FIRST agent they contact.</p>
    <p>When you choose me to list your home for sale, you can rest assured that I will contact each lead immediately and maximize the exposure to serious buyers. With cutting-edge systems in place to help manage perspective buyers, no potential lead will ever be lost.</p>
  </div>
</div>

<div class="card back" style="left:248px;top:930px;width:354px;height:238px">
  <div class="divider"></div>
  <div class="stamp"></div>
  <div class="header">
    <div class="portrait" role="img" aria-label="Agent portrait"></div>
    <div class="contact"><div class="call">Call Today!</div><div class="name">MARLA QUINN</div><div class="phone">555-014-2290</div><div class="web">hello@marlaquinnhomes.com<br>www.harborcountyhomes.example</div><div class="tagline">With you every step of the way!</div></div>
    <div class="brand"><span class="brand-mark"></span><div class="brand-name">Harbor Point Homes</div><div class="address">1820 Harbor Lane<br>Bayport, NC 28500</div></div>
  </div>
  <div class="pledge">
    <h3>Complete Confidentiality &amp; No Obligation Pledge</h3>
    <p>Meetings, assessments and correspondence are kept solely between the homeowner and/or the designated representative and do not require a commitment. It is our passion to respond promptly to real estate questions and see creative solutions no matter how great the vision.</p>
  </div>
</div>
<div class="label back-label" style="left:660px;top:1022px">BACK</div>

</body>
</html>
```